Ember Relaywork - Field Service Brochure

We are looking for a one page marketing brochure that includes our rate sheet. I've attached the working we on on the rate page, several photos and several versions of our logo.

```html
<!DOCTYPE html>
<html lang="en">
<head>
<meta charset="utf-8">
<title>Ember Relaywork – Field Service Brochure</title>
<link href="https://fonts.googleapis.com/css2?family=Montserrat:wght@500;700;800&family=Open+Sans:wght@400;600;700&display=swap" rel="stylesheet">
<style>
  :root{
    --page-bg:#e9eaec;
    --paper:#ffffff;
    --navy:#1f2f52;
    --slate:#62778f;
    --slate-dark:#4d6079;
    --slate-deep:#3e5068;
    --orange:#e9a23b;
    --card:#f4f5f7;
    --ink:#2b3340;
    --muted:#5a6472;
    --soft-white:#e8edf3;
  }
  *{box-sizing:border-box;margin:0;padding:0}
  html,body{width:1200px;height:3200px;overflow:hidden;background:var(--page-bg)}
  body{position:relative;font-family:"Open Sans",Arial,sans-serif;color:var(--ink)}

  .brochure{
    position:absolute;left:80px;top:927px;width:1040px;height:1346px;
    background:var(--paper);overflow:hidden;
    box-shadow:0 6px 24px rgba(0,0,0,.12);
  }

  /* header */
  .masthead{position:relative;height:450px;background:linear-gradient(180deg,#ffffff 0%,#f1f2f4 100%)}
  .masthead-photo{
    position:absolute;right:0;top:0;width:560px;height:300px;
    background:radial-gradient(ellipse at 60% 45%,rgba(190,196,204,.55) 0%,rgba(225,228,232,.35) 45%,rgba(255,255,255,0) 75%);
  }
  .brand{position:absolute;left:84px;top:72px;display:flex;align-items:center;gap:22px}
  .brand-square{width:118px;height:118px;border:6px solid var(--navy);background:var(--paper)}
  .brand-name{font-family:"Montserrat",Arial,sans-serif;font-weight:800;font-size:40px;letter-spacing:2px;color:var(--navy);text-transform:uppercase}
  .brand-sub{font-family:"Open Sans",Arial,sans-serif;font-size:14px;color:var(--muted);margin-top:4px;border-top:2px solid var(--navy);padding-top:6px}
  .intro{
    position:absolute;left:84px;right:84px;top:250px;
    font-size:18px;line-height:1.55;color:var(--ink);
  }

  /* rates */
  .rates{
    position:absolute;left:0;top:450px;width:100%;height:380px;
    background:var(--slate);display:flex;justify-content:center;gap:40px;padding-top:50px;
  }
  .rate-card{display:flex;width:290px;height:280px;box-shadow:0 4px 10px rgba(0,0,0,.18)}
  .rate-tab{
    width:44px;background:var(--navy);color:#fff;display:flex;align-items:center;justify-content:center;
    border-radius:10px 0 0 10px;
  }
  .rate-tab--accent{background:var(--orange)}
  .rate-tab span{writing-mode:vertical-rl;transform:rotate(180deg);font-family:"Montserrat",Arial,sans-serif;font-size:13px;font-weight:700;letter-spacing:1px;text-transform:uppercase}
  .rate-body{flex:1;background:var(--card);border-radius:0 10px 10px 0;padding:26px 16px;text-align:center;display:flex;flex-direction:column;justify-content:space-around}
  .rate-price{font-family:"Montserrat",Arial,sans-serif;font-weight:700;font-size:15px;color:var(--navy)}
  .rate-note{font-size:13px;line-height:1.35;color:var(--muted)}
  .rate-note strong{color:var(--ink)}
  .rate-body--text{text-align:center;justify-content:space-evenly}

  /* lower */
  .details{
    position:absolute;left:0;top:830px;width:100%;height:516px;
    background:linear-gradient(180deg,var(--slate-dark) 0%,var(--slate-deep) 100%);
  }
  .details h2{position:absolute;left:84px;top:34px;font-family:"Montserrat",Arial,sans-serif;font-size:20px;font-weight:700;color:#fff}
  .checklist{position:absolute;left:84px;top:76px;width:820px;list-style:none}
  .checklist li{display:flex;gap:12px;align-items:flex-start;font-size:14px;line-height:1.4;color:var(--soft-white);margin-bottom:8px}
  .checklist svg{flex:none;margin-top:2px}
  .contact{position:absolute;left:84px;top:262px;list-style:none}
  .contact li{display:flex;align-items:center;gap:14px;font-size:14px;color:var(--soft-white);margin-bottom:14px}
  .field-photo{
    position:absolute;right:0;bottom:0;width:600px;height:300px;
    border-top-left-radius:420px 190px;
    background:linear-gradient(160deg,#cfe0ef 0%,#8fb2d3 40%,#5e7f9f 70%,#c7652f 100%);
  }
</style>
</head>
<body>
<main class="brochure">
  <header class="masthead">
    <div class="masthead-photo" role="img" aria-label="Faint photo of line workers on a utility pole under an overcast sky"></div>
    <div class="brand">
      <div class="brand-square"></div>
      <div>
        <div class="brand-name">Ember Relaywork</div>
        <div class="brand-sub">A Northline Power Group Company</div>
      </div>
    </div>
    <p class="intro">Ember Relaywork offers an expert trained Field Service program that can provide technical guidance and assistance for your initial installation, sustaining maintenance and repair of equipment manufactured by Ember Relaywork. A 4–6 week reservation for assistance is recommended to ensure that we can fully accommodate your desired schedule. Expedited service may be available upon request.</p>
  </header>

  <section class="rates">
    <article class="rate-card">
      <div class="rate-tab"><span>Standard Rates</span></div>
      <div class="rate-body">
        <div><div class="rate-price">$XXX x 1.00</div><div class="rate-note">Monday through Friday 7am–4pm<br><strong>$XXXX Minimum</strong></div></div>
        <div><div class="rate-price">$XXX x 1.50</div><div class="rate-note">Monday through Friday after hours</div></div>
        <div><div class="rate-price">$XXX x 2.00</div><div class="rate-note">Sundays and Holidays</div></div>
      </div>
    </article>
    <article class="rate-card">
      <div class="rate-tab rate-tab--accent"><span>Travel Rates</span></div>
      <div class="rate-body">
        <div><div class="rate-price">$XXX x 1.00</div><div class="rate-note">Travel Time (door to door) per hour</div></div>
        <div><div class="rate-price">$XXX x 1.50</div><div class="rate-note">Travel Time Prior to Normal Hours</div></div>
        <div><div class="rate-price">$XXX x 2.00</div><div class="rate-note">Sunday and Holiday Travel Time</div></div>
      </div>
    </article>
    <article class="rate-card">
      <div class="rate-tab"><span>Expenses</span></div>
      <div class="rate-body rate-body--text">
        <div class="rate-note">Airfare – invoiced at cost plus 10% handling</div>
        <div class="rate-note">Lodging – invoiced at cost plus 10%</div>
        <div class="rate-note">Rental car and fuel billed at cost plus handling</div>
        <div class="rate-note">Meals and incidentals per diem rate</div>
      </div>
    </article>
  </section>

  <section class="details">
    <h2>Minimum Charge</h2>
    <ul class="checklist">
      <li><svg width="16" height="16" viewBox="0 0 16 16"><path d="M2 8l4 4 8-9" fill="none" stroke="#e9a23b" stroke-width="2.4"/></svg>Four hour minimum applies to every service call made during normal working hours.</li>
      <li><svg width="16" height="16" viewBox="0 0 16 16"><path d="M2 8l4 4 8-9" fill="none" stroke="#e9a23b" stroke-width="2.4"/></svg>Cancellations within 48 hours of scheduled service will be billed at the minimum charge.</li>
      <li><svg width="16" height="16" viewBox="0 0 16 16"><path d="M2 8l4 4 8-9" fill="none" stroke="#e9a23b" stroke-width="2.4"/></svg>Waiting time on site is billed at the applicable hourly rate.</li>
      <li><svg width="16" height="16" viewBox="0 0 16 16"><path d="M2 8l4 4 8-9" fill="none" stroke="#e9a23b" stroke-width="2.4"/></svg>Parts and materials are quoted separately and are not included in service rates shown above.</li>
    </ul>
    <ul class="contact">
      <li><svg width="16" height="18" viewBox="0 0 16 18"><path d="M8 1a5 5 0 015 5c0 4-5 11-5 11S3 10 3 6a5 5 0 015-5z" fill="#fff"/><circle cx="8" cy="6" r="2" fill="#4d6079"/></svg>1840 Foundry Lane<br>Westbrook, OH 44021</li>
      <li><svg width="16" height="16" viewBox="0 0 16 16"><path d="M3 1h3l1 4-2 1a9 9 0 005 5l1-2 4 1v3a2 2 0 01-2 2A13 13 0 011 3a2 2 0 012-2z" fill="#fff"/></svg>555-014-2280</li>
      <li><svg width="16" height="16" viewBox="0 0 16 16"><path d="M3 1h3l1 4-2 1a9 9 0 005 5l1-2 4 1v3a2 2 0 01-2 2A13 13 0 011 3a2 2 0 012-2z" fill="#fff"/></svg>555-014-2291</li>
      <li><svg width="16" height="16" viewBox="0 0 16 16"><rect x="1" y="3" width="14" height="10" fill="#fff"/><path d="M1 3l7 6 7-6" fill="none" stroke="#4d6079" stroke-width="1.4"/></svg>service@emberrelaywork.com</li>
      <li><svg width="16" height="16" viewBox="0 0 16 16"><circle cx="8" cy="8" r="6.5" fill="none" stroke="#fff" stroke-width="1.6"/><path d="M1.5 8h13M8 1.5c3 3 3 10 0 13M8 1.5c-3 3-3 10 0 13" fill="none" stroke="#fff" stroke-width="1.2"/></svg>emberrelaywork.com</li>
    </ul>
    <div class="field-photo" role="img" aria-label="Photo of field technicians in an orange bucket lift working on substation switchgear against a blue sky"></div>
  </section>
</main>
</body>
</html>
```